Buchcover-Design für Fantasy-Serie
Inspirierte und saubere Umsetzung, sowie kundenorientiert auch bei Sonderwünschen.
Zielgruppe
Buchverlag (Kleinstverlag). Wir verlegen Bücher aus den Genres Fantasy / SciFi / Thriller und Kriminalroman, sowie spezielle thematische Ausgaben. Kern unserer Tätigkeit ist die Wiederveröffentlichung der Nebelhorn-Chronik des deutschen Fantasy Autors Konrad Tilling sowie eine SciFi Serie des deutschen Autor Enno Braxmeyer. Wir suchen genretypische Cover mit Whow-Effekt.
Aufgabenstellung
Bei unserem ersten Auftrag handelt es sich um eine Fantasy Serie, bestehend aus 8 Bänden, welche vorwiegend als Kindle / eBook aber auch als Paperback veröffentlicht werden. Das Titelmotiv stammt jedes Mal von Laurent Dubelcq (lizensiert) und ändert sich bei jedem Buch. Der Titel muss daher von uns bearbeitbar sein.
das EBook hat die üblichen Maße: 1600x2560, 72 dpi
Print wird voraussichtl. 12x19, aber wir benötigen nur den Titel in 300 DPI (identisch mit Ebook lediglich höhere Auflösung).
Text:
(Autorenname): Konrad Tilling
(Buchtitel): Der Zirkel von Quasmar
(Titelzusatz): Erster Roman der Nebelhorn-Chronik
(Gattung): Roman
(Verlagslogo): Wahlweise kleines oder großes Logo, farblich angepasst
Hinweis: bei Auftrag wird das Titelbild in hoher Auflösung von uns geliefert.

```html
<!DOCTYPE html>
<html lang="de">
<head>
<meta charset="utf-8">
<title>Der Zirkel von Quasmar – Buchumschlag</title>
<link rel="stylesheet" href="https://fonts.googleapis.com/css2?family=Marcellus&family=Fjalla+One&family=Arvo:wght@700&family=Crimson+Text&display=swap">
<style>
  :root {
    --stage: #cfcfcf;
    --navy-deep: #051a2c;
    --navy: #0b2b4a;
    --spine-blue: #0f3d68;
    --band-blue: #003a6b;
    --accent-blue: #1a86c4;
    --sky-blue: #2aa3e8;
    --ink: #0c1524;
    --paper: #f3f3f4;
    --paper-edge: #c9ccd2;
    --art-edge: #0e2035;
    --white: #ffffff;
  }
  html, body {
    margin: 0;
    width: 1200px;
    height: 1200px;
    overflow: hidden;
    background: var(--stage);
  }
  .spread {
    position: absolute;
    left: 102px;
    top: 230px;
    width: 996px;
    height: 740px;
    box-shadow: 0 2px 6px rgba(0,0,0,.25);
  }
  /* Back cover */
  .back-cover {
    position: absolute;
    left: 0; top: 0;
    width: 468px; height: 740px;
    overflow: hidden;
  }
  .back-art {
    position: absolute; inset: 0;
    background:
      radial-gradient(ellipse 30% 14% at 88% 88%, rgba(150,175,200,.35), transparent 75%),
      radial-gradient(ellipse 40% 25% at 30% 78%, rgba(80,110,140,.35), transparent 75%),
      radial-gradient(ellipse 35% 40% at 62% 82%, rgba(4,18,32,.6), transparent 75%),
      radial-gradient(ellipse 70% 25% at 40% 35%, rgba(40,75,110,.35), transparent 75%),
      linear-gradient(180deg, #04182a 0%, #061d31 25%, #0d2d49 55%, #123a58 78%, #0a2a44 100%);
  }
  .publisher-mark {
    position: absolute;
    font-family: "Marcellus", serif;
    color: var(--white);
    letter-spacing: 1px;
    white-space: nowrap;
    text-transform: uppercase;
  }
  .back-cover .publisher-mark {
    left: 242px; top: 220px;
    transform: translateX(-50%);
    font-size: 17px;
  }
  .blurb {
    position: absolute;
    left: 100px; top: 250px;
    width: 284px; height: 270px;
    box-sizing: border-box;
    padding: 17px 20px 0 20px;
    background: rgba(12,52,90,.7);
    border: 1px solid rgba(150,190,225,.6);
    border-radius: 18px 0 18px 0;
    color: var(--white);
    font-family: "Crimson Text", serif;
    font-size: 10.3px;
    line-height: 14px;
    text-align: justify;
  }
  .blurb p { margin: 0 0 14px; }

  /* Spine */
  .spine {
    position: absolute;
    left: 468px; top: 0;
    width: 60px; height: 740px;
    background: var(--spine-blue);
  }
  .spine-title {
    position: absolute;
    left: 10px; top: 48px;
    writing-mode: vertical-rl;
    font-family: "Marcellus", serif;
    font-size: 25px;
    letter-spacing: 1.5px;
    color: var(--white);
    white-space: nowrap;
  }
  .spine-title .accent { color: var(--sky-blue); }
  .spine-label {
    position: absolute;
    left: 19px; top: 522px;
    width: 21px; height: 62px;
    background: var(--band-blue);
    writing-mode: vertical-rl;
    font-family: "Fjalla One", sans-serif;
    font-size: 12px;
    letter-spacing: 2px;
    color: var(--sky-blue);
    text-align: center;
    line-height: 21px;
  }
  .spine-author {
    position: absolute;
    left: 19px; top: 590px;
    width: 22px; height: 150px;
    box-sizing: border-box;
    background: var(--navy-deep);
    border: 1px solid rgba(255,255,255,.6);
    border-bottom: none;
    writing-mode: vertical-rl;
    font-family: "Arvo", serif;
    font-weight: 700;
    font-size: 13px;
    color: var(--white);
    line-height: 20px;
    padding-top: 12px;
    white-space: nowrap;
  }

  /* Front cover */
  .front-cover {
    position: absolute;
    left: 528px; top: 0;
    width: 468px; height: 740px;
    overflow: hidden;
    background: radial-gradient(ellipse 70% 60% at 50% 40%, var(--white) 0%, var(--paper) 45%, var(--paper-edge) 100%);
  }
  .front-art {
    position: absolute;
    left: 0; top: 350px;
    width: 468px; height: 390px;
    background:
      radial-gradient(ellipse 22% 9% at 80% 77%, rgba(235,240,246,.85), transparent 75%),
      radial-gradient(ellipse 30% 22% at 22% 50%, rgba(215,226,238,.75), transparent 72%),
      radial-gradient(ellipse 45% 28% at 35% 28%, rgba(165,182,202,.7), transparent 75%),
      radial-gradient(ellipse 22% 40% at 55% 55%, rgba(22,36,52,.75), transparent 75%),
      radial-gradient(ellipse 30% 55% at 88% 42%, rgba(10,20,32,.85), transparent 75%),
      radial-gradient(ellipse 60% 20% at 30% 92%, rgba(20,40,60,.8), transparent 80%),
      linear-gradient(180deg, var(--art-edge) 0%, #2b4058 18%, #4a6078 40%, #34495f 65%, #1c3045 88%, #13263a 100%);
  }
  .brush-edge { position: absolute; left: 0; width: 468px; }
  .brush-top { top: 0; height: 80px; }
  .brush-bottom { top: 335px; height: 40px; }
  .front-cover .publisher-mark {
    left: 234px; top: 30px;
    transform: translateX(-50%);
    font-size: 17px;
  }
  .title-block {
    position: absolute;
    left: 0; top: 115px;
    width: 468px;
    margin: 0;
    font-weight: 400;
    text-align: center;
    font-family: "Marcellus", serif;
  }
  .title-lead {
    display: flex; align-items: center; justify-content: center;
    gap: 14px;
    font-size: 36px; line-height: 40px;
    color: var(--ink);
  }
  .title-lead .rule { width: 76px; height: 2px; background: var(--band-blue); }
  .title-main {
    font-size: 40px; line-height: 42px;
    letter-spacing: 5px;
    color: var(--accent-blue);
  }
  .title-tail {
    font-size: 38px; line-height: 42px;
    color: var(--ink);
  }
  .subtitle {
    position: absolute;
    left: 82px; top: 260px;
    width: 304px;
    border-top: 2px solid var(--band-blue);
    border-bottom: 1px solid #8a9bb0;
    padding: 9px 0 7px;
    text-align: center;
    font-family: "Fjalla One", sans-serif;
    font-size: 17.5px;
    letter-spacing: .6px;
    color: var(--ink);
  }
  .author-bar {
    position: absolute;
    left: 0; top: 691px;
    width: 468px; height: 29px;
    display: flex;
    border-top: 1px solid rgba(150,190,225,.6);
    border-bottom: 1px solid rgba(150,190,225,.6);
  }
  .author-label {
    width: 180px;
    background: var(--band-blue);
    font-family: "Fjalla One", sans-serif;
    font-size: 17px;
    letter-spacing: 2px;
    color: var(--sky-blue);
    text-align: right;
    padding-right: 14px;
    box-sizing: border-box;
    line-height: 29px;
  }
  .author-name {
    flex: 1;
    background: var(--navy-deep);
    border-left: 1px solid rgba(255,255,255,.7);
    font-family: "Arvo", serif;
    font-weight: 700;
    font-size: 19px;
    letter-spacing: 1px;
    color: var(--white);
    padding-left: 13px;
    line-height: 29px;
  }
</style>
</head>
<body>
<div class="spread">
  <section class="back-cover">
    <div class="back-art" role="img" aria-label="Abgedunkeltes Titelmotiv: Felslandschaft mit steinernen Kolossen, verschneiter Klippe und Sturmhimmel"></div>
    <div class="publisher-mark">Nebelkamm</div>
    <div class="blurb">
      <p>Lorem ipsum dolor sit amet, consectetuer adipiscing elit, sed diam nonummy nibh euismod tincidunt ut laoreet dolore magna aliquam erat volutpat. Ut wisi enim ad minim veniam, quis nostrud exerci tation ullamcorper suscipit lobortis nisl ut aliquip ex ea commodo consequat. Duis autem vel eum iriure dolor in hendrerit in vulputate velit esse molestie consequat, vel illum dolore eu feugiat nulla facili</p>
      <p>Lorem ipsum dolor sit amet, consectetuer adipiscing elit, sed diam nonummy nibh euismod tincidunt ut laoreet dolore magna aliquam erat volutpat. Ut wisi enim ad minim veniam, quis nostrud exerci tation ullamcorper suscipit lobortis nisl ut aliquip ex ea commodo consequat. Duis autem vel eum iriure dolor in hendrerit in vulputate velit esse molestie consequat, vel illum dolore eu feugiat nulla facili</p>
    </div>
  </section>

  <section class="spine">
    <div class="spine-title">DER ZIRKEL <span class="accent">VON QUASMAR</span></div>
    <div class="spine-label">Author</div>
    <div class="spine-author">Konrad Tilling</div>
  </section>

  <section class="front-cover">
    <div class="front-art" role="img" aria-label="Titelmotiv: zwei steinerne Kolosse an einer Felswand, verschneite Klippe mit Tannen unter stürmischem, nebligem Himmel"></div>
    <svg class="brush-edge brush-top" viewBox="0 0 468 80" preserveAspectRatio="none" aria-hidden="true">
      <path fill="var(--band-blue)" d="M0 0H468V42L440 46 410 50 380 48 350 56 320 52 290 60 250 57 210 64 170 60 130 68 90 64 50 72 20 70 0 76Z"/>
    </svg>
    <svg class="brush-edge brush-bottom" viewBox="0 0 468 40" preserveAspectRatio="none" aria-hidden="true">
      <path fill="var(--art-edge)" d="M0 26 30 20 60 24 100 16 140 20 180 12 220 14 260 8 300 6 340 4 380 2 420 1 468 0V40H0Z"/>
    </svg>
    <div class="publisher-mark">Nebelkamm</div>
    <h1 class="title-block">
      <div class="title-lead"><span class="rule"></span>DER<span class="rule"></span></div>
      <div class="title-main">ZIRKEL</div>
      <div class="title-tail">VON QUASMAR</div>
    </h1>
    <div class="subtitle">Erster Roman der Nebelhorn-Chronik</div>
    <div class="author-bar">
      <div class="author-label">Author</div>
      <div class="author-name">Konrad Tilling</div>
    </div>
  </section>
</div>
</body>
</html>
```